Software engineering company needs business card

I need a cool business card. Company: Soft Belan Brindlewood Ave 41 58207 Sincity Name: Gerald Vanholt CEO / Managing Director & Owner

```html
<!DOCTYPE html>
<html lang="en">
<head>
<meta charset="utf-8">
<title>Soft Belan – Business Card</title>
<link rel="stylesheet" href="https://fonts.googleapis.com/css2?family=Raleway:wght@300;400&display=swap">
<style>
  :root {
    --backdrop: #4d5456;
    --card-white: #f4f4f4;
    --band-grey: #5f5f60;
    --brand-green: #8cc63f;
    --text-light: #dcdcdc;
    --divider: #d6d6d6;
    --mark-grey: #555657;
  }
  * { margin: 0; padding: 0; box-sizing: border-box; }
  html, body {
    width: 1200px; height: 737px; overflow: hidden;
    background: var(--backdrop);
    font-family: "Raleway", Arial, sans-serif;
  }
  .canvas { position: relative; width: 1200px; height: 737px; }

  .card {
    position: absolute;
    background: var(--card-white);
    overflow: hidden;
  }
  .card--front { left: 60px; top: 240px; width: 502px; height: 286px; }
  .card--back  { left: 635px; top: 241px; width: 500px; height: 288px; }

  .brand {
    position: absolute;
    left: 0; right: 0;
    display: flex; align-items: center; justify-content: center;
    gap: 14px;
  }
  .card--front .brand { top: 70px; }
  .card--back .brand  { top: 122px; }
  .brand__square {
    width: 22px; height: 22px;
    background: var(--mark-grey);
  }
  .brand__name {
    font-weight: 400;
    font-size: 34px;
    letter-spacing: 5px;
    color: var(--brand-green);
    text-transform: uppercase;
    line-height: 1;
  }

  .info-band {
    position: absolute;
    left: 0; top: 154px; width: 100%; height: 132px;
    background: var(--band-grey);
    color: var(--text-light);
    font-weight: 300;
  }
  .person { position: absolute; left: 28px; top: 20px; }
  .person__name {
    font-size: 18px; font-weight: 300;
    color: var(--brand-green);
    line-height: 1.1;
  }
  .person__title { font-size: 11.5px; margin-top: 2px; }
  .address { position: absolute; left: 28px; top: 85px; font-size: 11.5px; }

  .divider {
    position: absolute; left: 260px; top: 18px;
    width: 1px; height: 84px;
    background: var(--divider);
  }

  .contacts {
    position: absolute; left: 307px; top: 25px;
    list-style: none;
    font-size: 11px;
  }
  .contacts li {
    display: flex; align-items: center;
    height: 18.7px;
  }
  .contacts svg {
    width: 12px; height: 12px;
    margin-right: 12px;
    fill: none; stroke: var(--text-light); stroke-width: 1.3;
  }
</style>
</head>
<body>
<div class="canvas">

  <section class="card card--front">
    <div class="brand">
      <span class="brand__square"></span>
      <span class="brand__name">Soft Belan</span>
    </div>

    <div class="info-band">
      <div class="person">
        <p class="person__name">Gerald Vanholt</p>
        <p class="person__title">CEO / Geschäftsführer &amp; Inhaber</p>
      </div>
      <p class="address">Brindlewood Ave 41 58207 Sincity</p>

      <div class="divider"></div>

      <ul class="contacts">
        <li>
          <svg viewBox="0 0 12 12"><path d="M1 4.5c0-2 10-2 10 0v1H8.5V4h-5v1.5H1z" fill="#dcdcdc"/><rect x="3" y="6" width="6" height="4.5" fill="#dcdcdc" stroke="none"/></svg>
          (555) 214-7390
        </li>
        <li>
          <svg viewBox="0 0 12 12"><rect x="2.5" y="1" width="7" height="10" rx="1.5"/></svg>
          (000) 000-0000
        </li>
        <li>
          <svg viewBox="0 0 12 12"><rect x="0.8" y="2.5" width="10.4" height="7"/><path d="M0.8 2.5 6 6.5l5.2-4M0.8 9.5 4.5 5.5M11.2 9.5 7.5 5.5"/></svg>
          gvanholt@softbelan.dev
        </li>
        <li>
          <svg viewBox="0 0 12 12"><circle cx="6" cy="6" r="5"/><ellipse cx="6" cy="6" rx="2.2" ry="5"/><path d="M1 6h10M1.8 3.5h8.4M1.8 8.5h8.4"/></svg>
          www.softbelan.dev
        </li>
      </ul>
    </div>
  </section>

  <section class="card card--back">
    <div class="brand">
      <span class="brand__square"></span>
      <span class="brand__name">Soft Belan</span>
    </div>
  </section>

</div>
</body>
</html>
```